Business Cards

Business cards (double-sided) to be handed out to clients and potential clients, with contact details, logo .

Target Market(s)

Small to medium size businesses

Industry/Entity Type

Accountants

Contact Information for Business Card

Brightmere Ledger Accounting & Advisory Ltd

Colors

Designer to choose only greyscale colors for use in the design.

Requirements
Must have
• Name, Title, Address, Phone number, Email, Website
Nice to have
• Modern, clean lines, classy
Should not have
• Business cards to be double-sided. Form keeps reverting to single-sided.

```html
<!DOCTYPE html>
<html lang="en">
<head>
<meta charset="utf-8">
<title>Brightmere Ledger – Business Cards</title>
<link href="https://fonts.googleapis.com/css2?family=Arimo:wght@400;700&family=Montserrat:wght@400;500&display=swap" rel="stylesheet">
<style>
  :root{
    --bg:#e4e4e4;
    --charcoal:#2f2f2f;
    --charcoal-deep:#222;
    --paper:#ffffff;
    --ink:#2b2b2b;
    --rule:#555;
    --light:#f2f2f2;
  }
  *{margin:0;padding:0;box-sizing:border-box}
  html,body{width:1200px;height:802px;overflow:hidden;background:var(--bg)}
  .stage{position:relative;width:1200px;height:802px;display:flex;align-items:center;justify-content:center;gap:56px}
  .card{position:relative;width:520px;height:298px;box-shadow:0 10px 24px rgba(0,0,0,.18);overflow:hidden}

  /* front */
  .card--front{display:flex;background:var(--paper)}
  .front__brand{width:44%;background:var(--charcoal);display:flex;align-items:center;justify-content:center}
  .wordmark{display:flex;align-items:center;gap:10px;color:var(--light);font-family:"Montserrat",sans-serif;font-weight:500;letter-spacing:.12em;text-transform:uppercase}
  .wordmark__square{width:10px;height:10px;background:var(--light);flex:none}
  .wordmark__name{font-size:15px;line-height:1.35}
  .front__details{flex:1;display:flex;align-items:center;justify-content:center}
  .details-frame{border:1px solid var(--rule);padding:20px 22px;font-family:"Arimo",sans-serif;color:var(--ink);width:236px}
  .person__name{font-weight:700;font-size:17px;letter-spacing:.02em;text-transform:uppercase;white-space:nowrap}
  .person__title{font-size:13px;margin-top:2px}
  .address{font-size:13px;line-height:1.35;margin-top:14px}
  .contact{list-style:none;margin-top:12px;font-size:12.5px}
  .contact li{display:flex;align-items:center;gap:8px;line-height:1.6;white-space:nowrap}
  .contact svg{width:11px;height:11px;flex:none}

  /* back */
  .card--back{background:var(--charcoal-deep)}
  .back__texture{position:absolute;inset:0;background:linear-gradient(135deg,#2a2a2a 0%,#1f1f1f 55%,#262626 100%)}
  .back__brand{position:absolute;right:46px;top:50%;transform:translateY(-50%)}
  .back__brand .wordmark__name{font-size:13px}
</style>
</head>
<body>
<main class="stage">
  <section class="card card--front" aria-label="Business card front">
    <div class="front__brand">
      <div class="wordmark">
        <span class="wordmark__square"></span>
        <span class="wordmark__name">Brightmere<br>Ledger</span>
      </div>
    </div>
    <div class="front__details">
      <div class="details-frame">
        <p class="person__name">Daniel Ashford</p>
        <p class="person__title">Manager</p>
        <p class="address">Your Address, City<br>State, Zip 0000</p>
        <ul class="contact">
          <li><svg viewBox="0 0 12 12"><circle cx="6" cy="6" r="6" fill="#2b2b2b"/><path d="M4 3.2l1 1.4-.6.7a4 4 0 0 0 2.3 2.3l.7-.6 1.4 1-.6 1A5 5 0 0 1 3 3.8z" fill="#fff"/></svg>555-018-2740</li>
          <li><svg viewBox="0 0 12 12"><rect x="0.5" y="2" width="11" height="8" fill="#2b2b2b"/><path d="M1 2.5l5 4 5-4" stroke="#fff" fill="none"/></svg>hello@brightmereledger.com</li>
          <li><svg viewBox="0 0 12 12"><circle cx="6" cy="6" r="6" fill="#2b2b2b"/><circle cx="6" cy="6" r="3.6" stroke="#fff" fill="none"/><path d="M2.4 6h7.2M6 2.4v7.2" stroke="#fff"/></svg>www.brightmereledger.com</li>
        </ul>
      </div>
    </div>
  </section>

  <section class="card card--back" aria-label="Business card back">
    <div class="back__texture" role="img" aria-label="Tonal embossed repeat pattern across the dark card back"></div>
    <div class="back__brand wordmark">
      <span class="wordmark__square"></span>
      <span class="wordmark__name">Brightmere<br>Ledger</span>
    </div>
  </section>
</main>
</body>
</html>
```